Window Decal Design

I have office windows that need a design incorporating from my logo. It should be semi transparent and offer enough privacy for meetings.

Size of the window is 450cm by 295cm

Colors
F0912C
F2A743
F7CA91
FBE8D2
FDF5EE

```html
<!DOCTYPE html>
<html lang="en">
<head>
<meta charset="utf-8">
<title>Orvane — Window Decal</title>
<link href="https://fonts.googleapis.com/css2?family=Montserrat:wght@600&display=swap" rel="stylesheet">
<style>
  :root {
    --stage: #e6e7e9;
    --panel-light: #ffffff;
    --panel-mid: #ececec;
    --panel-shade: #dcdcdc;
    --orange: #ec7c2c;
    --gold: #e9a545;
    --charcoal: #54575a;
    --white: #ffffff;
  }
  html, body {
    margin: 0;
    padding: 0;
    width: 960px;
    height: 1200px;
    overflow: hidden;
    background: var(--stage);
  }
  .canvas {
    position: relative;
    width: 960px;
    height: 1200px;
    display: flex;
    align-items: center;
    justify-content: center;
  }
  .window-decal {
    width: 880px;
    height: 578px;
    display: block;
    box-shadow: 4px 4px 6px rgba(0, 0, 0, 0.45);
  }
  .brand-name {
    font-family: "Montserrat", sans-serif;
    font-weight: 600;
    font-size: 120px;
    fill: var(--charcoal);
    letter-spacing: 4px;
  }
</style>
</head>
<body>
  <main class="canvas">
    <svg class="window-decal" viewBox="0 0 1370 900" xmlns="http://www.w3.org/2000/svg" aria-label="Orvane window decal">
      <defs>
        <linearGradient id="panel-fill" x1="0" y1="0" x2="1" y2="1">
          <stop offset="0" stop-color="var(--panel-mid)"/>
          <stop offset="0.45" stop-color="var(--panel-light)"/>
          <stop offset="1" stop-color="var(--panel-mid)"/>
        </linearGradient>
        <clipPath id="panel-clip">
          <rect width="1370" height="900"/>
        </clipPath>
      </defs>

      <g clip-path="url(#panel-clip)">
        <rect class="panel-base" width="1370" height="900" fill="url(#panel-fill)"/>

        <g class="soft-arcs" fill="var(--panel-shade)">
          <circle cx="300" cy="-260" r="680" opacity="0.25"/>
          <circle cx="1140" cy="980" r="640" opacity="0.35"/>
          <circle cx="1320" cy="1180" r="640" opacity="0.25"/>
        </g>

        <path class="orange-band" d="M0 665 Q700 790 1370 495 L1370 900 L0 900 Z" fill="var(--orange)"/>
        <path class="white-swoosh" d="M0 652 Q700 778 1370 482" fill="none" stroke="var(--white)" stroke-width="14"/>
        <path class="gold-swoosh" d="M0 636 Q700 752 1370 466" fill="none" stroke="var(--gold)" stroke-width="9"/>
      </g>

      <g class="brand-lockup">
        <circle class="brand-dot" cx="455" cy="318" r="34" fill="var(--orange)"/>
        <text class="brand-name" x="515" y="360">Orvane</text>
      </g>
    </svg>
  </main>
</body>
</html>
```